Harbor Bug Guard Business Cards

A modern business card with a predominantly white background and a sleek design featuring Harbor with complimentary greys or blacks to convey a professional and contemporary look.

Front:
Primarily white background. Limited use of company purple color can be neighbored by greys.
Text: Name, Title, Cell Phone, Office Phone, Website, email address

Back:
Background Continuation: The back of the card maintains the white background for consistency.
Company name “Harbor” in company color and font, “Bug Guard” underneath or underneath left justified of “Harbor.”
A subtle pattern or texture in shades of grey to add depth behind the company Logo in font.

logo color: hex #6212ab
font: antique olive nord D Regular

```html
<!DOCTYPE html>
<html lang="en">
<head>
<meta charset="utf-8">
<title>Harbor Bug Guard Business Cards</title>
<link rel="stylesheet" href="https://fonts.googleapis.com/css2?family=Montserrat:wght@400;500;700;800&display=swap">
<style>
  :root {
    --brand: #6212ab;
    --ink: #222222;
    --grey: #a9a9a9;
    --divider: #cfcfcf;
    --card: #ffffff;
    --backdrop: #d5d5d5;
  }
  * { box-sizing: border-box; margin: 0; padding: 0; }
  html, body {
    width: 1200px; height: 913px; overflow: hidden;
    background: var(--backdrop);
    font-family: "Montserrat", Arial, sans-serif;
  }
  .canvas { position: relative; width: 1200px; height: 913px; }
  .card {
    position: absolute;
    width: 600px; height: 343px;
    background: var(--card);
    border: 2px solid var(--brand);
    border-radius: 30px;
    box-shadow: 0 18px 40px rgba(0,0,0,0.22);
  }
  .card--front { left: 90px; top: 90px; display: flex; align-items: center; }
  .card--back { left: 510px; top: 480px; display: flex; align-items: center; justify-content: center; }

  .identity { flex: none; width: 290px; padding-left: 70px; }
  .identity__name {
    color: var(--brand); font-weight: 800; font-size: 28px;
    line-height: 1.1; white-space: nowrap;
  }
  .identity__title { color: var(--ink); font-size: 17px; margin-top: 6px; white-space: nowrap; }

  .divider { flex: none; width: 1px; height: 96px; background: var(--divider); margin: 0 22px 0 12px; }

  .contacts { list-style: none; }
  .contacts__item {
    display: flex; align-items: center; gap: 10px;
    color: var(--ink); font-size: 15px; line-height: 1; margin: 9px 0;
    white-space: nowrap;
  }
  .contacts__icon { width: 15px; height: 15px; fill: var(--brand); flex: none; }

  .wordmark { display: flex; align-items: center; gap: 20px; }
  .wordmark__dot { width: 46px; height: 46px; border-radius: 50%; background: var(--brand); flex: none; }
  .wordmark__text {
    color: var(--brand); font-weight: 800; font-size: 46px;
    line-height: 1.02; text-transform: uppercase; letter-spacing: 1px;
    white-space: nowrap;
  }
</style>
</head>
<body>
<main class="canvas">
  <section class="card card--front" aria-label="Card front">
    <div class="identity">
      <p class="identity__name">Tova Renning</p>
      <p class="identity__title">Managing Director</p>
    </div>
    <div class="divider"></div>
    <ul class="contacts">
      <li class="contacts__item">
        <svg class="contacts__icon" viewBox="0 0 16 16"><path d="M2 6c0-2 2-3 6-3s6 1 6 3v1h-3V6H5v1H2zM3 8h10l1 6H2z"/></svg>
        044-555 010 123
      </li>
      <li class="contacts__item">
        <svg class="contacts__icon" viewBox="0 0 16 16"><path d="M4 1h8a1 1 0 0 1 1 1v12a1 1 0 0 1-1 1H4a1 1 0 0 1-1-1V2a1 1 0 0 1 1-1zm1 2v9h6V3z"/></svg>
        044-555 010 124
      </li>
      <li class="contacts__item">
        <svg class="contacts__icon" viewBox="0 0 16 16"><path d="M1 3h14v10H1zm1.5 1.2V12h11V4.2L8 8.5z"/></svg>
        info@harborbugguard.com
      </li>
      <li class="contacts__item">
        <svg class="contacts__icon" viewBox="0 0 16 16"><path d="M8 1a7 7 0 1 0 0 14A7 7 0 0 0 8 1zm0 1.4c.9 0 1.9 1.9 2.1 4.6H5.9C6.1 4.3 7.1 2.4 8 2.4zM2.5 9h2.1c.1 1.6.5 3 1 3.9A5.6 5.6 0 0 1 2.5 9zm0-2a5.6 5.6 0 0 1 3.1-3.9c-.5.9-.9 2.3-1 3.9zm5.5 6.6c-.9 0-1.9-1.9-2.1-4.6h4.2c-.2 2.7-1.2 4.6-2.1 4.6zm2.4-.7c.5-.9.9-2.3 1-3.9h2.1a5.6 5.6 0 0 1-3.1 3.9zM11.4 7c-.1-1.6-.5-3-1-3.9A5.6 5.6 0 0 1 13.5 7z"/></svg>
        www.harborbugguard.com
      </li>
    </ul>
  </section>

  <section class="card card--back" aria-label="Card back">
    <div class="wordmark">
      <span class="wordmark__dot"></span>
      <p class="wordmark__text">Harbor<br>Bug Guard</p>
    </div>
  </section>
</main>
</body>
</html>
```